Black Granite Web Design Project

We are looking for a design for a new company that will be selling Black Granite slabs and tiles. We will be selling to both end-consumers and granite installers. We have already settled on a logo and hopefully this will give an idea of what we like in our designs. We are not going to be selling online but want people to call us so the site is basically an enhanced business card. We will be focusing a lot on SEO so the design will have to keep that in mind.

We would like to keep the design in 1024x768 to make it easily view-able on all devices.

Regarding navigation there should only be a few sub-pages, like "Granite Slabs", "Granite Tiles", "Delivery", "Contact"

Aside from that we are open to designs. One idea we did have was to personalize the site and have a person there somehow to represent the company, making the user feel there are real people behind this site. This is just an idea and not a must.

The name of the company and site is "Copper Ridge Pietra"

Thanks
Updates

Hello All,

Thanks for the great designs. There are some good looking designs that show beautiful kitchens but this site is made for the granite installers and not the retail consumers. So in order not to to confuse the buyers I would like to keep this as much about the raw products as possible. The raw products being the granite slabs, thereby making it obvious we don't sell granite counter tops. 

This design will really be the identity of this company so it is important we get the right message across on this index page and that this page is as complete as possible.

Again, thanks for all the work being put into this.

Target Market(s)

The target audience is granite installers or companies that would with granite slabs.

Industry/Entity Type

Business

```html
<!DOCTYPE html>
<html lang="en">
<head>
<meta charset="utf-8">
<title>Copper Ridge Pietra</title>
<link rel="stylesheet" href="https://fonts.googleapis.com/css2?family=Oswald:wght@500;600&family=Arimo:wght@400;700&family=Questrial&display=swap">
<style>
:root{
  --black:#000;
  --white:#fff;
  --gold:#dba840;
  --gold-text:#e0ab3c;
  --panel-grey:#d0d0d0;
  --body-text:#4a4a4a;
  --blue:#1b74b0;
}
*{margin:0;padding:0;box-sizing:border-box}
html,body{width:768px;height:1200px;overflow:hidden;background:var(--black)}
.page{position:relative;width:768px;height:1200px;overflow:hidden;background:var(--black);font-family:"Arimo",Arial,sans-serif}
.abs{position:absolute}

/* header */
.logo{left:96px;top:34px;width:128px;text-align:center;color:var(--white)}
.logo-mark{display:inline-block;width:14px;height:14px;background:var(--white);margin-bottom:4px}
.logo-name{font-family:"Oswald",sans-serif;font-weight:600;font-size:13px;letter-spacing:.2px;line-height:1.1}
.logo-place{font-size:5px;letter-spacing:1.5px;margin-top:2px}
.nav{top:51px;left:0;color:var(--white);font-size:14px}
.nav a{position:absolute;color:var(--white);text-decoration:none;white-space:nowrap}

/* phone tab */
.call-tab{left:0;top:270px;width:30px;height:52px;background:var(--gold);border-radius:0 4px 4px 0;display:flex;align-items:center;justify-content:center}

/* tiled backdrop */
.tiles{left:0;top:348px;width:768px;height:390px}

/* hero */
.hero{left:65px;top:110px;width:665px;height:352px;background:var(--black);border:1px solid #777;overflow:hidden}
.hero-photo{position:absolute;left:0;top:0;width:400px;height:352px;background:radial-gradient(ellipse at 45% 55%,#9a9a9a 0%,#4d4d4d 40%,#111 75%,#000 100%)}
.hero-title{position:absolute;left:367px;top:145px;display:flex;align-items:flex-end;color:var(--gold);font-family:"Oswald",sans-serif;font-weight:600;line-height:.9}
.hero-title .big{font-size:52px;letter-spacing:-.5px}
.hero-title .small{font-size:25px;margin-left:8px;padding-bottom:3px}
.hero-band{position:absolute;left:367px;top:212px;width:298px;height:47px;background:var(--white);border-left:18px solid var(--gold);font-family:"Oswald",sans-serif;font-weight:500;font-size:23px;color:var(--black);padding-left:10px;line-height:47px;letter-spacing:-.3px;white-space:nowrap}

/* about band */
.about-rule{left:222px;top:486px;width:325px;height:1px;background:#555}
.section-title{font-weight:700;font-size:17px;white-space:nowrap}
.about-title{left:0;width:768px;top:505px;text-align:center;color:var(--black)}
.clients-title{left:109px;top:576px;width:255px;line-height:22px;color:var(--black);white-space:normal}
.world-map{left:47px;top:626px;width:90px;height:58px;background:radial-gradient(ellipse,#222 0%,#444 55%,rgba(0,0,0,0) 72%)}
.client-list{left:150px;top:625px;font-family:"Questrial",sans-serif;font-size:12px;line-height:14px;color:var(--body-text);list-style:none}
.price-icon{left:394px;top:567px}
.price-title{left:446px;top:579px;color:var(--black)}
.price-text{left:403px;top:627px;width:347px;font-family:"Questrial",sans-serif;font-size:12px;line-height:13.5px;color:var(--body-text)}

/* dark section */
.dark-title{left:0;width:768px;top:770px;text-align:center;color:var(--white)}
.dark-rule{top:786px;width:143px;height:1px;background:#aaa}

.grid{left:54px;top:812px;width:664px;height:293px;display:grid;grid-template-columns:221px 222px 221px;grid-template-rows:148px 145px}
.cell{position:relative;overflow:hidden}
.granite{background:radial-gradient(circle at 30% 30%,#2b2b2b,#0c0c0c 70%)}
.stonewall{background:linear-gradient(160deg,#e4dccb,#c9bfac 50%,#a69c8b)}
.lounge{background:linear-gradient(180deg,#d8d8d8 0%,#9a9a9a 45%,#2a2a2a 100%)}
.offer{background:var(--panel-grey);padding:24px 0 0 32px}
.offer-head{font-family:"Oswald",sans-serif;font-weight:600;font-size:22px;color:var(--black);display:flex;align-items:flex-end;gap:6px;padding-left:15px}
.offer-head .num{font-size:40px;line-height:.9;font-weight:500}
.offer-head .unit{font-family:"Arimo",sans-serif;font-weight:400;font-size:19px}
.offer-text{margin-top:14px;font-size:12px;line-height:15px;color:var(--black);width:185px}
.card{background:var(--gold)}
.card-title{font-family:"Oswald",sans-serif;font-weight:600;color:var(--white);letter-spacing:-.5px;white-space:nowrap}
.care .card-title{font-size:22px;position:absolute;left:36px;top:24px}
.care .card-text{position:absolute;left:33px;top:64px;width:170px;text-align:center;font-size:12.5px;line-height:15px;color:var(--black)}
.like .card-title{font-size:20px;position:absolute;left:13px;top:15px}
.like .card-text{position:absolute;left:16px;top:56px;width:170px;font-family:"Questrial",sans-serif;font-size:11.5px;line-height:13.5px;color:var(--black)}
.icon-strip{position:absolute;right:0;bottom:0;display:flex}
.icon-strip span{width:29px;height:30px;display:flex;align-items:center;justify-content:center;background:var(--white);border-left:1px solid #ccc}
.icon-strip span.dark{background:#000;border:none}

.footer{left:0;width:768px;top:1162px;text-align:center;color:var(--gold-text);font-size:10.5px;padding-left:37px}
</style>
</head>
<body>
<div class="page">

  <header>
    <div class="abs logo">
      <span class="logo-mark"></span>
      <div class="logo-name">COPPER RIDGE PIETRA</div>
      <div class="logo-place">SERRA ALTA</div>
    </div>
    <nav class="abs nav">
      <a href="#" style="left:306px">Home</a>
      <a href="#" style="left:379px">Granite Slabs</a>
      <a href="#" style="left:485px">Granite Tiles</a>
      <a href="#" style="left:589px">Delivery</a>
      <a href="#" style="left:665px">Contact</a>
    </nav>
  </header>

  <svg class="abs tiles" viewBox="0 0 768 390" aria-hidden="true">
    <rect width="768" height="390" fill="#d4d4d4"/>
    <rect x="107" y="115" width="220" height="150" fill="#bdbdbd"/>
    <rect x="327" y="115" width="220" height="150" fill="#a9a9a9"/>
    <rect x="547" y="100" width="221" height="110" fill="#b2b2b2"/>
    <rect x="730" y="20" width="38" height="80" fill="#c6c6c6"/>
    <g fill="#bcbcbc">
      <rect x="0" y="94" width="768" height="4"/>
      <rect x="0" y="192" width="768" height="4"/>
      <rect x="0" y="288" width="768" height="4"/>
      <rect x="105" y="98" width="4" height="292"/>
      <rect x="218" y="190" width="4" height="200"/>
      <rect x="326" y="190" width="4" height="200"/>
      <rect x="437" y="190" width="4" height="200"/>
      <rect x="547" y="190" width="4" height="200"/>
      <rect x="658" y="220" width="4" height="170"/>
    </g>
    <rect x="0" y="388" width="768" height="2" fill="#999"/>
  </svg>

  <div class="abs call-tab" aria-label="Call us">
    <svg width="22" height="22" viewBox="0 0 22 22"><circle cx="11" cy="11" r="9.5" fill="none" stroke="#fff" stroke-width="2"/><path d="M7 14.5l2-1.5 1.5 1c1.8-1 3.3-2.5 4-4l-1-1.5 1.5-2" fill="none" stroke="#fff" stroke-width="2" stroke-linecap="round"/></svg>
  </div>

  <section class="abs hero">
    <div class="hero-photo" role="img" aria-label="Black and white photo of a stonemason working a granite block with a pneumatic tool"></div>
    <h1 class="hero-title"><span class="big">COPPER</span><span class="small">RIDGE<br>PIETRA</span></h1>
    <div class="hero-band">WE HAVE NO-LIMIT IN DESIGN</div>
  </section>

  <div class="abs about-rule"></div>
  <h2 class="abs section-title about-title">ABOUT MY HISTORY AND PRICES</h2>

  <h3 class="abs section-title clients-title">MY CLIENTS ARE LOCATED EVERYWHERE</h3>
  <div class="abs world-map" role="img" aria-label="World map with client locations marked in green"></div>
  <ul class="abs client-list">
    <li>United States</li>
    <li>Manila (Philippines)</li>
    <li>Canada</li>
    <li>India</li>
  </ul>

  <svg class="abs price-icon" width="36" height="36" viewBox="0 0 36 36" aria-hidden="true"><circle cx="18" cy="18" r="18" fill="var(--blue)"/><text x="18" y="25" text-anchor="middle" font-family="Arimo,sans-serif" font-weight="700" font-size="21" fill="#fff">$</text></svg>
  <h3 class="abs section-title price-title">HOW MUCH DO I CHARGE?</h3>
  <p class="abs price-text">I get the majority of my work through referrals, and I have references available at your request. The rest of my business comes from this short letter and its associated advertisement on Searchly.</p>

  <div class="abs dark-rule" style="left:53px"></div>
  <h2 class="abs section-title dark-title">ABOUT MY HISTORY AND PRICES</h2>
  <div class="abs dark-rule" style="left:574px"></div>

  <section class="abs grid">
    <div class="cell granite" role="img" aria-label="Close-up of speckled black granite">
      <div class="icon-strip">
        <span class="dark"><svg width="18" height="18" viewBox="0 0 18 18"><circle cx="9" cy="9" r="8" fill="#fff"/><rect x="8" y="7.5" width="2" height="6" fill="#000"/><circle cx="9" cy="5" r="1.2" fill="#000"/></svg></span>
        <span><svg width="12" height="12" viewBox="0 0 12 12"><circle cx="2" cy="10" r="1.5" fill="#333"/><path d="M1 5.5a5.5 5.5 0 0 1 5.5 5.5M1 1.5a9.5 9.5 0 0 1 9.5 9.5" fill="none" stroke="#333" stroke-width="1.6"/></svg></span>
        <span><svg width="12" height="12" viewBox="0 0 12 12"><circle cx="6" cy="6" r="4" fill="#333"/></svg></span>
        <span><svg width="12" height="12" viewBox="0 0 12 12"><rect x="1" y="2" width="10" height="9" fill="none" stroke="#333"/><rect x="1" y="2" width="10" height="2" fill="#333"/><path d="M3 6h6M3 8h6" stroke="#333" stroke-width=".8"/></svg></span>
      </div>
    </div>
    <div class="cell offer">
      <div class="offer-head"><span>OFFER</span><span class="num">1</span><span class="unit">YEAR</span></div>
      <p class="offer-text">YOU CAN JOIN US EVEN YOUR SALE 1 YEAR</p>
    </div>
    <div class="cell stonewall" role="img" aria-label="Stacked beige stone wall cladding">
      <div class="icon-strip">
        <span class="dark"><svg width="18" height="18" viewBox="0 0 18 18"><circle cx="9" cy="9" r="8" fill="#fff"/><rect x="8" y="7.5" width="2" height="6" fill="#000"/><circle cx="9" cy="5" r="1.2" fill="#000"/></svg></span>
        <span><svg width="12" height="12" viewBox="0 0 12 12"><circle cx="2" cy="10" r="1.5" fill="#333"/><path d="M1 5.5a5.5 5.5 0 0 1 5.5 5.5M1 1.5a9.5 9.5 0 0 1 9.5 9.5" fill="none" stroke="#333" stroke-width="1.6"/></svg></span>
        <span><svg width="12" height="12" viewBox="0 0 12 12"><circle cx="6" cy="6" r="4" fill="#333"/></svg></span>
        <span><svg width="12" height="12" viewBox="0 0 12 12"><rect x="1" y="2" width="10" height="9" fill="none" stroke="#333"/><rect x="1" y="2" width="10" height="2" fill="#333"/><path d="M3 6h6M3 8h6" stroke="#333" stroke-width=".8"/></svg></span>
      </div>
    </div>
    <div class="cell card care">
      <h3 class="card-title">WE CARE ABOUT U</h3>
      <p class="card-text">there, anywhere.Dorn is NOT directly affiliated with the V</p>
    </div>
    <div class="cell lounge" role="img" aria-label="Black and white photo of a chair and lounge bench in a sunlit room"></div>
    <div class="cell card like">
      <h3 class="card-title">LIKE your design</h3>
      <p class="card-text">ences available at your request. The rest of my business comes ences available at your request. The rest of my business comes .</p>
    </div>
  </section>

  <footer class="abs footer">ALLRIGHTS RESERVED BY YOUR COMPANY NAME 2013</footer>
</div>
</body>
</html>
```